VORELT B2B portal design
Fantastic design work, top communication and fast design changes! Many thanks,Jens & Uwe from VORELT
Zielgruppe
We are a B2B Cloud Services StartUp that creates B2B logistics & supply chain processes between customer and its suppliers.
Aufgabenstellung
We need a modern responsive able design, that should consider that we are NOT presenting goods or clothes or similar on the portal pages but we show mainly data grids, kpi dashboards, forms, and setting panels to our customer and their suppliers.
The design must be clean and straight not to distract people from the important information in these data grids, kpi dashboards, forms, and settings panels.
We need our logo perfectly embedded and the pages coloured around from grey to blue.
The Designer must be able to deliver a design and transfer it to a highly responsive HTML (5) template (without technical content or further functionality). This our programmers will implement afterwards in .Net.
We need in total 3 page templates:
1. Login Page
2. Main Page with overview over the following services text (each one shown in one tile)
"ZMS (Time Frame Management)"
"DMS (Document Management)"
"REMS (Reporting Management)"
-> Note: At the end we will have up to 12 or more tiles (services) so the design should be additive
3. Data grid (e.g. list of customers)/form (e.g. customer registration form) page to show some data grid with database data
See samples for each page enclosed!!

```html
<!DOCTYPE html>
<html lang="en">
<head>
<meta charset="utf-8">
<title>VORELT – Services</title>
<link rel="stylesheet" href="https://fonts.googleapis.com/css2?family=Signika:wght@400;600&display=swap">
<style>
  :root {
    --navy: #0d2b45;
    --header-bg: #e2e7eb;
    --sidebar-bg: #e2e7eb;
    --main-bg: #f8f9fb;
    --divider: #c9d0d6;
    --text: #1c2b38;
    --muted: #555f68;
    --green: #5cb85c;
    --green-text: #4c9f46;
    --blue: #4cb0d2;
    --blue-text: #2f88a6;
    --orange: #f0ad4e;
    --orange-text: #d3821a;
    --white: #ffffff;
  }
  * { box-sizing: border-box; margin: 0; padding: 0; }
  html, body { width: 1200px; height: 1019px; overflow: hidden; }
  body {
    position: relative;
    background: var(--white);
    font-family: "Signika", "Segoe UI", sans-serif;
    color: var(--text);
  }
  .site-header {
    position: absolute; left: 0; top: 0; width: 1200px; height: 208px;
    background: var(--header-bg);
    border-bottom: 1px solid #9aa1a7;
  }
  .brand {
    position: absolute; left: 24px; top: 66px;
    display: flex; align-items: center; gap: 16px;
    font-size: 72px; font-weight: 600; letter-spacing: 2px;
    color: var(--navy); line-height: 1;
  }
  .brand-mark { width: 22px; height: 22px; background: var(--navy); border-radius: 50%; }
  .user-menu {
    position: absolute; right: 12px; top: 70px;
    display: flex; align-items: center; gap: 10px;
  }
  .user-info { text-align: right; }
  .user-name { font-size: 21px; font-weight: 600; color: var(--navy); line-height: 1.1; }
  .user-role { font-size: 14px; color: var(--muted); }
  .user-avatar {
    width: 68px; height: 68px; border-radius: 50%;
    background: radial-gradient(circle at 50% 40%, #8f8a86, #4a4644);
    border: 2px solid #b9bec2;
  }
  .caret { width: 0; height: 0; border-left: 5px solid transparent; border-right: 5px solid transparent; border-top: 6px solid #7a8086; }

  .sidebar {
    position: absolute; left: 0; top: 208px; width: 265px; height: 709px;
    background: var(--sidebar-bg);
  }
  .nav-item {
    display: flex; align-items: center; gap: 12px;
    height: 61px; padding-left: 20px;
    font-size: 20px; color: var(--text);
    border-bottom: 1px solid var(--divider);
  }
  .nav-item svg { width: 26px; height: 26px; fill: var(--navy); flex: none; }
  .nav-item.is-active {
    background: var(--navy); color: var(--white);
    height: 56px; margin: 4px 0; border-bottom: none;
    position: relative;
  }
  .nav-item.is-active svg { fill: var(--white); }
  .nav-item .chevron { position: absolute; right: 28px; top: 18px; width: 14px; height: 18px; fill: none; stroke: var(--white); stroke-width: 2.5; }
  .nav-item.no-border { border-bottom: none; }

  .content {
    position: absolute; left: 265px; top: 208px; width: 935px; height: 709px;
    background: var(--main-bg);
  }
  .service-tile {
    position: absolute; top: 81px; width: 265px; height: 220px;
    background: var(--white); border: 1px solid #d8dde2; border-radius: 3px;
    overflow: hidden; text-align: center;
    box-shadow: 0 1px 2px rgba(0,0,0,0.06);
  }
  .tile-visual { height: 157px; display: flex; align-items: center; justify-content: center; }
  .tile-visual svg { width: 120px; height: 120px; fill: none; stroke: var(--white); stroke-width: 5; stroke-linecap: round; stroke-linejoin: round; }
  .tile-title { font-size: 22px; font-weight: 600; margin-top: 8px; line-height: 1.1; }
  .tile-subtitle { font-size: 16px; margin-top: 2px; }
  .tile-zms { left: 39px; }
  .tile-zms .tile-visual { background: var(--green); }
  .tile-zms .tile-title, .tile-zms .tile-subtitle { color: var(--green-text); }
  .tile-dms { left: 339px; }
  .tile-dms .tile-visual { background: var(--blue); }
  .tile-dms .tile-title, .tile-dms .tile-subtitle { color: var(--blue-text); }
  .tile-rems { left: 638px; }
  .tile-rems .tile-visual { background: var(--orange); }
  .tile-rems .tile-title, .tile-rems .tile-subtitle { color: var(--orange-text); }

  .site-footer {
    position: absolute; left: 0; top: 958px; width: 1200px; height: 61px;
    border-top: 1px solid #eceff2;
    display: flex; justify-content: space-between; align-items: center;
    padding: 0 22px 0 14px;
    font-size: 17px; color: var(--muted);
  }
  .footer-links span { margin: 0 6px; }
</style>
</head>
<body>
  <header class="site-header">
    <div class="brand"><span class="brand-mark"></span>VORELT</div>
    <div class="user-menu">
      <div class="user-info">
        <div class="user-name">Lars Brenner</div>
        <div class="user-role">Gest User</div>
      </div>
      <div class="user-avatar" role="img" aria-label="User profile photo"></div>
      <div class="caret"></div>
    </div>
  </header>

  <nav class="sidebar">
    <div class="nav-item">
      <svg viewBox="0 0 26 26"><rect x="2" y="8" width="22" height="10" rx="2"/></svg>My News
    </div>
    <div class="nav-item">
      <svg viewBox="0 0 26 26"><circle cx="11" cy="8" r="6"/><path d="M1 25c0-7 4-10 10-10s10 3 10 10z"/></svg>My User Settings
    </div>
    <div class="nav-item">
      <svg viewBox="0 0 26 26"><circle cx="9" cy="9" r="7"/><circle cx="19" cy="19" r="5"/></svg>Company Settings
    </div>
    <div class="nav-item">
      <svg viewBox="0 0 26 26"><path d="M3 21l12-12 2 2-12 12z"/><path d="M20 2l4 4-6 6-4-4z"/></svg>Configuration
    </div>
    <div class="nav-item is-active">
      <svg viewBox="0 0 26 26"><rect x="2" y="3" width="5" height="5"/><rect x="9" y="3" width="15" height="5"/><rect x="2" y="10" width="5" height="5"/><rect x="9" y="10" width="15" height="5"/><rect x="2" y="17" width="5" height="5"/><rect x="9" y="17" width="15" height="5"/></svg>Services
      <svg class="chevron" viewBox="0 0 14 18"><path d="M4 3l6 6-6 6"/></svg>
    </div>
    <div class="nav-item">
      <svg viewBox="0 0 26 26"><ellipse cx="14" cy="11" rx="11" ry="8"/><path d="M4 24l3-8 6 3z"/></svg>Communication
    </div>
    <div class="nav-item no-border">
      <svg viewBox="0 0 26 26"><path d="M4 6h8v3H7v11h11v-5h3v8H4z"/><path d="M14 3h9v9l-3-3-6 6-3-3 6-6z"/></svg>Logout
    </div>
  </nav>

  <main class="content">
    <article class="service-tile tile-zms">
      <div class="tile-visual">
        <svg viewBox="0 0 120 120">
          <path d="M30 92A44 44 0 1 1 60 104"/>
          <path d="M30 80v14h14"/>
          <text x="60" y="70" text-anchor="middle" font-size="30" fill="#fff" stroke="none" font-family="Signika, sans-serif">24</text>
        </svg>
      </div>
      <h2 class="tile-title">ZMS</h2>
      <p class="tile-subtitle">Time Frame Management System</p>
    </article>
    <article class="service-tile tile-dms">
      <div class="tile-visual">
        <svg viewBox="0 0 120 120">
          <path d="M12 52l12-24h72l12 24"/>
          <rect x="12" y="52" width="96" height="56"/>
          <path d="M12 70h96"/>
          <circle cx="60" cy="88" r="6"/>
          <path d="M36 52V18h40l8 8v26"/>
          <path d="M46 8h30"/>
        </svg>
      </div>
      <h2 class="tile-title">DMS</h2>
      <p class="tile-subtitle">Document Management System</p>
    </article>
    <article class="service-tile tile-rems">
      <div class="tile-visual">
        <svg viewBox="0 0 120 120">
          <rect x="22" y="10" width="64" height="88"/>
          <path d="M94 22v86H34"/>
          <path d="M34 28h40M34 40h40"/>
          <path d="M34 80l14-14 12 8 16-18"/>
        </svg>
      </div>
      <h2 class="tile-title">REMS</h2>
      <p class="tile-subtitle">Reporting Management System</p>
    </article>
  </main>

  <footer class="site-footer">
    <div>© 2016 VORELT. All rights reserved.</div>
    <div class="footer-links">Help<span>/</span>Disclaimer<span>/</span>Contact</div>
  </footer>
</body>
</html>
```